Letterhead, business cards, envelopes
Thornwell Holdings Property Management
Creative Brief
Professional
Dean Pultorak
Real Estate Asset Manager
27816 Brisbane Ave., Los Alamitos Ca 90720
dean@thpropertymgmt.example
www.thpropertymgmt.example
designers choice

```html
<!DOCTYPE html>
<html lang="en">
<head>
<meta charset="utf-8">
<title>Thornwell Holdings Property Management — Stationery</title>
<link href="https://fonts.googleapis.com/css2?family=Cinzel:wght@600&family=Open+Sans:wght@400;600&display=swap" rel="stylesheet">
<style>
  :root {
    --backdrop: #6b4a25;
    --paper: #ffffff;
    --green: #1f8a4c;
    --green-dark: #0f5e31;
    --swoosh: #3a3a3a;
    --grey: #b9b9b9;
    --ink: #2b2b2b;
    --muted: #777777;
    --rule: #c8c8c8;
  }
  * { box-sizing: border-box; margin: 0; padding: 0; }
  html, body { width: 1200px; height: 530px; overflow: hidden; }
  body {
    background: var(--backdrop);
    font-family: "Open Sans", Arial, sans-serif;
    color: var(--ink);
    position: relative;
  }
  .sheet {
    position: absolute;
    background: var(--paper);
    box-shadow: 0 2px 6px rgba(0,0,0,.45);
    overflow: hidden;
  }
  .wave { position: absolute; left: 0; bottom: 0; width: 100%; }

  .brand { position: absolute; display: flex; align-items: center; gap: 6px; }
  .brand-square { background: var(--green-dark); flex: none; }
  .brand-name {
    font-family: "Cinzel", "Times New Roman", serif;
    font-weight: 600;
    color: var(--green-dark);
    line-height: 1.05;
    letter-spacing: .02em;
    white-space: nowrap;
  }

  .letterhead { left: 29px; top: 89px; width: 312px; height: 403px; }
  .fax { left: 379px; top: 89px; width: 312px; height: 403px; }
  .letterhead .brand, .fax .brand { left: 24px; top: 14px; }
  .letterhead .brand-square, .fax .brand-square { width: 22px; height: 22px; }
  .letterhead .brand-name, .fax .brand-name { font-size: 11px; }

  .footer-web {
    position: absolute; left: 16px; bottom: 16px;
    font-size: 5px; color: #fff; white-space: nowrap;
  }
  .footer-contact {
    position: absolute; right: 12px; bottom: 10px;
    font-size: 4.5px; color: #fff; text-align: right; line-height: 1.4;
  }

  .fax-title {
    position: absolute; left: 28px; top: 86px;
    font-size: 20px; font-weight: 600; line-height: 1; letter-spacing: .05em;
    white-space: nowrap;
  }
  .fax-fields {
    position: absolute; left: 28px; top: 116px; width: 258px;
    display: grid; grid-template-columns: 1fr 1fr; column-gap: 14px;
  }
  .fax-field {
    font-size: 5px; color: var(--muted);
    border-bottom: 1px solid var(--rule);
    padding: 6px 0 2px;
  }
  .fax-options {
    position: absolute; left: 28px; top: 198px; width: 258px;
    display: flex; justify-content: space-between;
  }
  .fax-option { display: flex; gap: 3px; font-size: 5px; color: var(--muted); line-height: 1.2; }
  .fax-option::before {
    content: ""; width: 5px; height: 5px; border: 1px solid var(--muted); flex: none;
  }

  .envelope-back { left: 744px; top: 10px; width: 432px; height: 196px; }
  .envelope-flap { position: absolute; left: 0; top: 0; width: 100%; height: 100%; }
  .envelope-front { left: 728px; top: 226px; width: 448px; height: 192px; }
  .envelope-front .brand { left: 16px; top: 14px; }
  .envelope-front .brand-square { width: 18px; height: 18px; }
  .envelope-front .brand-name { font-size: 9px; }
  .envelope-return {
    position: absolute; left: 16px; top: 46px;
    font-size: 4.5px; color: var(--muted); line-height: 1.4;
  }

  .card { top: 425px; width: 144px; height: 80px; }
  .card-front { left: 785px; }
  .card-back { left: 946px; }
  .card-front .brand { left: 8px; top: 8px; gap: 4px; }
  .card-front .brand-square { width: 12px; height: 12px; }
  .card-front .brand-name { font-size: 6px; }
  .card-person { position: absolute; left: 8px; top: 30px; font-size: 4.5px; line-height: 1.4; color: var(--ink); white-space: nowrap; }
  .card-person strong { font-weight: 600; }
  .card-back .brand-square { position: absolute; left: 56px; top: 12px; width: 30px; height: 30px; }
</style>
</head>
<body>

<svg width="0" height="0" style="position:absolute">
  <defs>
    <symbol id="wave-band" viewBox="0 0 300 60" preserveAspectRatio="none">
      <path d="M0,26 C90,52 190,8 300,2 L300,14 C190,18 100,56 0,38Z" fill="var(--swoosh)"/>
      <path d="M0,36 C95,60 195,16 300,11 L300,60 L0,60Z" fill="var(--green)"/>
      <path d="M0,44 C100,62 200,26 300,22" fill="none" stroke="#fff" stroke-width="1" opacity=".7"/>
    </symbol>
  </defs>
</svg>

<section class="sheet letterhead" aria-label="Letterhead">
  <div class="brand">
    <span class="brand-square"></span>
    <span class="brand-name">Thornwell Holdings<br>Property Management</span>
  </div>
  <svg class="wave" height="58"><use href="#wave-band"/></svg>
  <p class="footer-web">www.thpropertymgmt.example</p>
  <p class="footer-contact">27816 Brisbane Ave.<br>Los Alamitos Ca 90720<br>Tel (562) 555-0148</p>
</section>

<section class="sheet fax" aria-label="Fax cover sheet">
  <div class="brand">
    <span class="brand-square"></span>
    <span class="brand-name">Thornwell Holdings<br>Property Management</span>
  </div>
  <h1 class="fax-title">FAX</h1>
  <div class="fax-fields">
    <p class="fax-field">To:</p><p class="fax-field">From:</p>
    <p class="fax-field">Fax:</p><p class="fax-field">Pages:</p>
    <p class="fax-field">Phone:</p><p class="fax-field">Date:</p>
    <p class="fax-field">Re:</p><p class="fax-field">CC:</p>
  </div>
  <div class="fax-options">
    <span class="fax-option">Urgent</span>
    <span class="fax-option">For<br>Review</span>
    <span class="fax-option">Please<br>Comment</span>
    <span class="fax-option">Please<br>Reply</span>
    <span class="fax-option">Please<br>Recycle</span>
  </div>
  <svg class="wave" height="58"><use href="#wave-band"/></svg>
  <p class="footer-web">www.thpropertymgmt.example</p>
  <p class="footer-contact">27816 Brisbane Ave.<br>Los Alamitos Ca 90720<br>Fax (562) 555-0149</p>
</section>

<section class="sheet envelope-back" aria-label="Envelope back">
  <svg class="envelope-flap" viewBox="0 0 432 196" preserveAspectRatio="none">
    <defs>
      <linearGradient id="flap-shade" x1="0" y1="0" x2="0" y2="1">
        <stop offset="0" stop-color="#3b3b3b"/>
        <stop offset=".6" stop-color="#9a9a9a"/>
        <stop offset="1" stop-color="#e4e4e4"/>
      </linearGradient>
    </defs>
    <path d="M0,0 L432,0 L432,26 Q216,120 0,26Z" fill="url(#flap-shade)"/>
    <path d="M0,196 L150,96 L282,96 L432,196" fill="none" stroke="var(--rule)" stroke-width="1"/>
    <path d="M0,26 L170,110 M432,26 L262,110" stroke="var(--rule)" stroke-width="1"/>
  </svg>
</section>

<section class="sheet envelope-front" aria-label="Envelope front">
  <div class="brand">
    <span class="brand-square"></span>
    <span class="brand-name">Thornwell Holdings<br>Property Management</span>
  </div>
  <p class="envelope-return">27816 Brisbane Ave.<br>Los Alamitos Ca 90720</p>
  <svg class="wave" height="46"><use href="#wave-band"/></svg>
  <p class="footer-web">www.thpropertymgmt.example</p>
</section>

<section class="sheet card card-front" aria-label="Business card front">
  <div class="brand">
    <span class="brand-square"></span>
    <span class="brand-name">Thornwell Holdings<br>Property Management</span>
  </div>
  <p class="card-person"><strong>Dean Pultorak</strong><br>Real Estate Asset Manager<br>27816 Brisbane Ave., Los Alamitos Ca 90720<br>dean@thpropertymgmt.example</p>
  <svg class="wave" height="16"><use href="#wave-band"/></svg>
</section>

<section class="sheet card card-back" aria-label="Business card back">
  <span class="brand-square"></span>
  <svg class="wave" height="22"><use href="#wave-band"/></svg>
</section>

</body>
</html>
```